4 'Thank you' greetings cards designs

We are a small greetings card publisher and we need designs for a range of 'Thank you' greetings cards and notecards.
This project is for a total of 4 designs.
Please take a look at this board on Clipnest, to see the kind of thing we are looking for: https://www.pinboardly.example/marvk8150/gratitude-notes/
The cards will be printed at a maximum size of 131mm x 183mm (including a 3mm bleed) so please provide 300dpi CMYK files at this size. Please ensure that any text (or elements of the design that are not part of the bleed) are at least 11mm in from each edge. Also, please note that cards do not have to have a bleed if your design doesn't require it (e.g. a plain white background).
Please provide 2 designs in 'portrait' orientation and 2 in 'landscape'.
Please provide 2 designs that just have the words 'Thank you' and then 2 designs that include your choice of these alternative messages:
Thank you so much
Thanks very much
Thank you very much
Thanks a million
Just to say thank you
A big thank you
A really big thank you
Feel free to use an exclamation mark on a couple of your designs, if you wish!
Other than the above guidelines, everything else is up to you in terms of colours, fonts, shapes, etc. - but please use the Clipnest board to see the kind of designs we are looking for.
Thank you!

```html
<!DOCTYPE html>
<html lang="en">
<head>
<meta charset="utf-8">
<title>Thank you card range</title>
<link href="https://fonts.googleapis.com/css2?family=Antonio:wght@100&family=Playfair+Display:wght@700&family=Dancing+Script:wght@600&family=Caveat:wght@500&display=swap" rel="stylesheet">
<style>
  :root {
    --backdrop: #f4f0ef;
    --paper: #ffffff;
    --blush: #f6b8ad;
    --blush-light: #fbd9d3;
    --butter: #fbf3c4;
    --ink: #1a1a1a;
    --lilac: #b8a0bc;
    --lilac-deep: #a891ad;
    --chalk: #f7f3f8;
    --orange: #f08a1c;
    --purple: #8e4f9e;
    --red: #c8202f;
    --green: #5aa232;
    --blue: #2a9fd0;
    --heart-pink: #f0a7a0;
    --heart-yellow: #f6ee9c;
    --heart-mint: #8fd4c4;
    --heart-violet: #b7aadb;
  }
  * { margin: 0; padding: 0; box-sizing: border-box; }
  html, body { width: 1200px; height: 1200px; overflow: hidden; }
  body { background: var(--backdrop); position: relative; }

  .card { position: absolute; overflow: hidden; }

  /* Card 1: portrait, dotted bands */
  .card-dots { left: 118px; top: 69px; width: 403px; height: 531px; background: var(--paper); }
  .dot-band { position: absolute; left: 0; width: 100%; background: linear-gradient(var(--blush), var(--blush)); }
  .dot-band--top { top: 0; height: 146px; border-bottom: 12px solid var(--blush-light); }
  .dot-band--bottom { bottom: 0; height: 150px; border-top: 12px solid var(--blush-light); }
  .card-dots .message {
    position: absolute; left: 0; right: 0; top: 188px; text-align: center;
    font-family: "Antonio", sans-serif; font-weight: 100; font-size: 70px;
    line-height: 78px; color: var(--ink); letter-spacing: -1px;
  }

  /* Card 2: landscape, big multicolour */
  .card-big { left: 606px; top: 140px; width: 549px; height: 390px; background: var(--paper); }
  .card-big svg { position: absolute; inset: 0; }
  .big-message { position: absolute; font-family: "Playfair Display", serif; font-weight: 700; line-height: 1; }
  .big-message--a { left: 110px; top: 100px; font-size: 34px; color: var(--orange); }
  .big-message--big { left: 135px; top: 80px; font-size: 66px; letter-spacing: -3px; }
  .big-message--thank { left: 195px; top: 135px; font-size: 84px; letter-spacing: -4px; }
  .big-message--you { left: 328px; top: 222px; font-size: 70px; letter-spacing: -3px; }
  .c-orange { color: var(--orange); } .c-purple { color: var(--purple); }
  .c-red { color: var(--red); } .c-green { color: var(--green); } .c-blue { color: var(--blue); }

  /* Card 3: landscape, hearts */
  .card-hearts { left: 46px; top: 652px; width: 547px; height: 388px; }
  .heart-field {
    position: absolute; inset: 0;
    background:
      radial-gradient(ellipse 48% 42% at 50% 50%, #fbfbfb 55%, rgba(251,251,251,0) 100%),
      linear-gradient(135deg, var(--heart-pink), var(--heart-yellow) 30%, var(--heart-mint) 55%, var(--heart-violet) 80%, var(--heart-pink));
    opacity: 0.85;
  }
  .card-hearts .message {
    position: absolute; left: 0; right: 0; top: 160px; text-align: center;
    font-family: "Dancing Script", cursive; font-weight: 600; font-size: 54px; color: var(--ink);
  }

  /* Card 4: portrait, lilac burst */
  .card-burst {
    left: 681px; top: 612px; width: 399px; height: 529px;
    background: radial-gradient(ellipse at 50% 50%, var(--lilac) 40%, var(--lilac-deep) 100%);
  }
  .card-burst svg { position: absolute; inset: 0; }
  .card-burst .message {
    position: absolute; left: 0; right: 0; top: 100px; text-align: center;
    font-family: "Caveat", cursive; font-weight: 500; font-size: 86px; line-height: 74px;
    color: var(--chalk); transform: rotate(-3deg);
  }
</style>
</head>
<body>

  <section class="card card-dots">
    <div class="dot-band dot-band--top" role="img" aria-label="Pink band with a pattern of white painted polka dots"></div>
    <p class="message">THANK<br>YOU</p>
    <div class="dot-band dot-band--bottom" role="img" aria-label="Pink band with a pattern of white painted polka dots"></div>
  </section>

  <section class="card card-big">
    <svg width="549" height="390" viewBox="0 0 549 390">
      <circle cx="160" cy="390" r="230" fill="var(--butter)"/>
      <circle cx="515" cy="165" r="225" fill="var(--butter)"/>
    </svg>
    <span class="big-message big-message--a">a</span>
    <span class="big-message big-message--big"><span class="c-purple">B</span><span class="c-red">I</span><span class="c-green">G</span></span>
    <span class="big-message big-message--thank"><span class="c-red">t</span><span class="c-blue">h</span><span class="c-green">a</span><span class="c-orange">n</span><span class="c-purple">k</span></span>
    <span class="big-message big-message--you"><span class="c-red">y</span><span class="c-green">o</span><span class="c-blue">u</span></span>
  </section>

  <section class="card card-hearts">
    <div class="heart-field" role="img" aria-label="Scattered crayon-textured hearts in pink, yellow, mint and violet around a pale centre"></div>
    <p class="message">Thank you</p>
  </section>

  <section class="card card-burst">
    <svg width="399" height="529" viewBox="0 0 399 529">
      <g stroke="var(--chalk)" stroke-width="8" stroke-linecap="round" fill="none" opacity="0.9">
        <line x1="28" y1="36" x2="72" y2="84"/>
        <line x1="204" y1="20" x2="207" y2="66"/>
        <line x1="350" y1="36" x2="302" y2="104"/>
        <line x1="30" y1="244" x2="118" y2="252"/>
        <line x1="290" y1="272" x2="376" y2="266"/>
        <line x1="24" y1="496" x2="108" y2="434"/>
        <line x1="204" y1="470" x2="207" y2="514"/>
        <line x1="320" y1="444" x2="364" y2="498"/>
      </g>
    </svg>
    <p class="message">thank<br>you<br>very<br>much</p>
  </section>

</body>
</html>
```